Personal Chef Business Card Design

My company, Simmerly, is a personal in-home chef service that caters to clients' needs, but I am not a caterer. The types of services that I provide range from : weekly menus for busy families, special menus for specific diets, custom menus, private parties, intimate dinners, and brunch parties. My cooking style is seasonal and simple with the option of a variety of cuisines. I like colorful and simple business cards. My business is just getting started as I will be the only employee for now. I would like to be able to use the design on the card for my logo also. I don't know if logo design is a different service altogether.

If you can convince me to go with double-sided, then so be it, but until then, I'll stick with singe-sided.

Target Market(s)

busy families, health conscious, private parties, brunch parties, dinner parties

Industry/Entity Type

Chef

Contact Information for Business Card

Ross Tamblyn
rosstamblyn@mailvora.com
434-817-2290
Simmerly Personal Chef Service
Serving the DC/VA/MD area

Font styles to use
Serif
Sans Serif
Decorative
Script
Other font styles liked:
• Anything

Requirements
Must have
• I will be using the illustration as my logo so that I can use it for promotional merchandise.

```html
<!DOCTYPE html>
<html lang="en">
<head>
<meta charset="utf-8">
<title>Simmerly Business Card</title>
<link rel="stylesheet" href="https://fonts.googleapis.com/css2?family=Alegreya:wght@400;500&display=swap">
<style>
  :root {
    --backdrop: #e9e6e1;
    --card: #050505;
    --gold: #f2c94c;
    --gold-deep: #e0b53a;
    --wine: #a3252a;
    --ink-light: #e8e8e8;
  }
  * { margin: 0; padding: 0; box-sizing: border-box; }
  html, body {
    width: 1200px;
    height: 900px;
    overflow: hidden;
    background: var(--backdrop);
    font-family: "Alegreya", Georgia, serif;
  }
  .canvas { position: relative; width: 1200px; height: 900px; }
  .card {
    position: absolute;
    width: 620px;
    height: 354px;
    background: var(--card);
    box-shadow: 0 10px 24px rgba(0,0,0,0.25);
    overflow: hidden;
  }
  .card--front { left: 80px; top: 70px; }
  .card--back  { left: 500px; top: 476px; }

  .brand { position: absolute; display: flex; flex-direction: column; align-items: center; }
  .brand__square { width: 72px; height: 66px; background: var(--wine); }
  .brand__name {
    margin-top: 8px;
    color: var(--gold);
    font-weight: 400;
    font-size: 50px;
    letter-spacing: 2px;
    text-transform: uppercase;
    line-height: 1;
  }
  .card--front .brand { left: 0; right: 0; top: 108px; }
  .card--back .brand { right: 44px; top: 40px; }
  .card--back .brand__square { width: 62px; height: 56px; }
  .card--back .brand__name { font-size: 42px; }

  .person { position: absolute; left: 44px; top: 172px; }
  .person__name { color: var(--gold); font-size: 30px; font-weight: 500; line-height: 1.1; }
  .person__role { color: var(--ink-light); font-size: 16px; margin-top: 2px; }

  .contact {
    position: absolute;
    left: 44px;
    top: 252px;
    color: var(--ink-light);
    font-size: 16px;
    line-height: 1.6;
  }
  .contact__label { color: var(--gold-deep); }
  .contact__web { color: var(--gold-deep); margin-left: 14px; }
</style>
</head>
<body>
<main class="canvas">
  <section class="card card--front" aria-label="Card front">
    <div class="brand">
      <div class="brand__square"></div>
      <div class="brand__name">Simmerly</div>
    </div>
  </section>

  <section class="card card--back" aria-label="Card back">
    <div class="brand">
      <div class="brand__square"></div>
      <div class="brand__name">Simmerly</div>
    </div>
    <div class="person">
      <div class="person__name">Ross Tamblyn</div>
      <div class="person__role">Personal Chef Service</div>
    </div>
    <div class="contact">
      <div>Serving the DC/VA/MD area</div>
      <div><span class="contact__label">T:</span> 434-817-2290</div>
      <div>
        <span class="contact__label">E:</span> rosstamblyn@mailvora.com
        <span class="contact__web">www.simmerlychef.com</span>
      </div>
    </div>
  </section>
</main>
</body>
</html>
```